Best in class cloud software provider for retailers needs a new business card design to reflect prod

We are a software company based out of Chicago selling into retailers. We have a new website and marketing collateral that support our new product designs. We are obsessed with simplicity, ease of use, and having a really powerful product set. We have two products as noted on our website - www.brolvane.com - one is a retail task management product and the other is a Help Ticketing product.

At Brolvane we are passionate about creating the best Retail Task Management system in the industry. We bring more than 20 years of retail operations, Workforce Management and Retail Task experience and have a set of web and mobile software features that no one else has. Brolvane enables you to plan and distribute work throughout your organization and ensure it gets done.

We need a new business card design that reflects our new branding, message and approach.

I've attached a few documents that help support what we are building and how our colors look.

There may be additional future work if this goes well.

Thanks,
Mark

President

Target Market(s)

We sell into retailers and are a software company

Industry/Entity Type

Software

Contact Information for Business Card

The card must have

Name
title
address
tele
email
Brolvane logo (someplace)

So for example

It would have for me

Mark Dorsett
President
48 West Harlow Ave. Suite 310
Chicago, IL 60687
3125550187
mdorsett@brolvane.com

Requirements
Must have
• We need to cards for 5 different people - same design different names etc
Nice to have
• should reflect our colors and product and website - be creative - ease of use, simplicity, and power is what the product is about - but we are very forward Brolvane and hear all the time that our product is gorgeous. The font should be consistent with our website, and marketing one pager included
Should not have
• Strange or unfamiliar colors or fonts...

```html
<!DOCTYPE html>
<html lang="en">
<head>
<meta charset="utf-8">
<title>Brolvane Business Card</title>
<link href="https://fonts.googleapis.com/css2?family=Open+Sans:wght@400;700;800&display=swap" rel="stylesheet">
<style>
  :root {
    --brand-blue: #1f78a4;
    --brand-blue-light: #3a8fb8;
    --brand-orange: #ee6a2b;
    --card-white: #fbfbfa;
    --page-bg: #e4e6e8;
    --text-blue: #1d6f98;
  }
  * { box-sizing: border-box; margin: 0; padding: 0; }
  html, body {
    width: 1200px; height: 800px; overflow: hidden;
    background: var(--page-bg);
    font-family: "Open Sans", Arial, sans-serif;
  }
  .sheet {
    width: 1200px; height: 800px;
    display: flex; align-items: center; justify-content: center; gap: 40px;
  }
  .card {
    position: relative;
    width: 540px; height: 309px;
    background: var(--card-white);
    box-shadow: 0 6px 18px rgba(0,0,0,0.18);
    overflow: hidden;
  }
  .card-back { display: flex; align-items: center; justify-content: center; }
  .wordmark {
    font-weight: 800;
    letter-spacing: 1px;
    line-height: 1;
    white-space: nowrap;
  }
  .card-back .wordmark { color: var(--brand-blue); font-size: 64px; }
  .card-front .swoosh { position: absolute; inset: 0; }
  .card-front .wordmark {
    position: absolute; right: 30px; top: 92px;
    color: var(--brand-orange); font-size: 50px;
  }
  .holder {
    position: absolute; left: 34px; bottom: 30px;
    color: #fff; line-height: 1.25;
  }
  .holder .name { font-size: 20px; }
  .holder .title { font-size: 15px; }
  .contact {
    position: absolute; right: 24px; top: 168px;
    list-style: none; text-align: right;
    color: var(--text-blue); font-size: 11.5px; line-height: 19px;
  }
  .contact li { display: flex; align-items: center; justify-content: flex-end; gap: 6px; white-space: nowrap; }
  .contact svg, .address svg { width: 10px; height: 10px; fill: var(--brand-orange); flex: none; }
  .address {
    position: absolute; right: 24px; bottom: 22px;
    display: flex; align-items: center; gap: 6px;
    color: var(--text-blue); font-size: 10.5px; white-space: nowrap;
  }
</style>
</head>
<body>
<main class="sheet">
  <section class="card card-back" aria-label="Card back">
    <span class="wordmark">Brolvane</span>
  </section>

  <section class="card card-front" aria-label="Card front">
    <svg class="swoosh" viewBox="0 0 540 309" aria-hidden="true">
      <defs>
        <radialGradient id="blueGlow" cx="0.6" cy="0.55" r="0.7">
          <stop offset="0" stop-color="var(--brand-blue-light)"/>
          <stop offset="1" stop-color="var(--brand-blue)"/>
        </radialGradient>
      </defs>
      <path d="M0,0 L150,0 Q165,250 270,309 L0,309 Z" fill="url(#blueGlow)"/>
      <path d="M163,0 Q178,240 288,309" fill="none" stroke="var(--brand-orange)" stroke-width="6"/>
    </svg>

    <span class="wordmark">Brolvane</span>

    <ul class="contact">
      <li>3125550187
        <svg viewBox="0 0 12 12"><circle cx="6" cy="3.5" r="2.6"/><path d="M1 12 Q1 6.5 6 6.5 Q11 6.5 11 12 Z"/></svg></li>
      <li>mdorsett@brolvane.com
        <svg viewBox="0 0 12 12"><rect x="0.5" y="2" width="11" height="8"/><path d="M0.5 2 L6 7 L11.5 2" stroke="#fff" stroke-width="1" fill="none"/></svg></li>
      <li>www.brolvane.com
        <svg viewBox="0 0 12 12"><circle cx="6" cy="6" r="5.5"/><path d="M0.5 6 H11.5 M6 0.5 V11.5" stroke="#fff" stroke-width="0.9"/></svg></li>
    </ul>
    <p class="address">48 West Harlow Ave. Suite 310 Chicago, IL 60687
      <svg viewBox="0 0 12 12"><path d="M6 1 L12 6.5 H10 V11 H2 V6.5 H0 Z"/></svg></p>

    <div class="holder">
      <p class="name">Mark Dorsett</p>
      <p class="title">President</p>
    </div>
  </section>
</main>
</body>
</html>
```